Update Business Card Design

I'm looking to update my business cards. Attached is a photo of the current design. I like the black side so that does not have to be update. The white side needs to be updated. I want the design to be modern and minimalistic.
I am a lawyer and my firm's website is www.brennoxlegalco.com (for reference).
My firm's logo has a horizontal version (which is on the black side of the card) and a vertical version (on the white side). I would prefer to keep the vertical version on the white side and horizontal version on the black side (the logo files are attached).

I am open to redesigning the black side also. I would like one side to have the horizontal logo and the other to have the vertical logo.

```html
<!DOCTYPE html>
<html lang="en">
<head>
<meta charset="utf-8">
<title>Brennox Legal Co — Business Card</title>
<link href="https://fonts.googleapis.com/css2?family=Poppins:wght@400;700&display=swap" rel="stylesheet">
<style>
  :root{
    --stage:#2b2b2b;
    --card:#131313;
    --accent:#00b2e3;
    --ink:#f2f2f2;
    --muted:#cfcfcf;
    --silver:#e6e6e6;
  }
  *{margin:0;padding:0;box-sizing:border-box}
  html,body{width:1200px;height:689px;overflow:hidden;background:var(--stage);font-family:"Poppins",sans-serif}
  .canvas{position:relative;width:1200px;height:689px}
  .card{position:absolute;top:190px;width:540px;height:309px;border-radius:22px;overflow:hidden;background:var(--card)}
  .card--front{left:40px}
  .card--back{left:620px}
  .pattern{position:absolute;inset:0;background:linear-gradient(115deg,var(--silver) 0%,#9a9a9a 28%,#3a3a3a 50%,#0c0c0c 70%,#000 100%)}
  .brand{position:absolute;display:flex;align-items:center;gap:10px;color:var(--accent);font-weight:700;letter-spacing:.08em;text-transform:uppercase}
  .brand__mark{width:14px;height:14px;background:var(--accent)}
  .card--front .brand{left:50%;top:50%;transform:translate(-50%,-50%);font-size:20px;background:var(--card);padding:12px 20px;border-radius:6px}
  .card--back .brand{right:34px;top:36px;font-size:22px}
  .identity{position:absolute;left:34px;top:118px;padding-left:20px}
  .identity::before{content:"";position:absolute;left:0;top:6px;width:9px;height:44px;background:var(--accent)}
  .identity__name{color:var(--accent);font-weight:700;font-size:26px;line-height:1.15}
  .identity__title{color:var(--ink);font-size:13px}
  .contacts{position:absolute;left:54px;top:190px;list-style:none}
  .contacts li{display:flex;align-items:center;gap:10px;color:var(--ink);font-size:12.5px;line-height:19px}
  .contacts svg{width:12px;height:12px;fill:var(--accent);flex:none}
  .address{position:absolute;right:34px;top:218px;color:var(--ink);font-size:12.5px;line-height:20px;font-style:normal;text-align:left}
</style>
</head>
<body>
<main class="canvas">
  <section class="card card--front">
    <div class="pattern" role="img" aria-label="Glossy repeating monogram pattern fading from silver to black"></div>
    <div class="brand"><span class="brand__mark"></span>Brennox Legal Co</div>
  </section>

  <section class="card card--back">
    <div class="brand"><span class="brand__mark"></span>Brennox Legal Co</div>
    <div class="identity">
      <h1 class="identity__name">Daniel Marrow</h1>
      <p class="identity__title">Attorney at Law</p>
    </div>
    <ul class="contacts">
      <li><svg viewBox="0 0 12 12"><path d="M3 0h6a1 1 0 0 1 1 1v10a1 1 0 0 1-1 1H3a1 1 0 0 1-1-1V1a1 1 0 0 1 1-1zm0 1.5v8h6v-8z"/></svg>310.555.0142</li>
      <li><svg viewBox="0 0 12 12"><path d="M1 4c0-2 2-3 5-3s5 1 5 3l-2 1-1-1.5H4L3 5zM2 6l2-1.5h4L10 6v5H2z"/></svg>310.555.0178</li>
      <li><svg viewBox="0 0 12 12"><path d="M3 0h5v3H3zM1 4h10v8H1zm2 2v1h2V6zm4 0v1h2V6zM3 8v1h2V8zm4 0v1h2V8z"/></svg>310.555.0193</li>
      <li><svg viewBox="0 0 12 12"><path d="M0 2h12v8H0zm1 1 5 4 5-4z"/></svg>daniel@brennoxlegalco.com</li>
      <li><svg viewBox="0 0 12 12"><circle cx="6" cy="6" r="6"/></svg>www.brennoxlegalco.com</li>
    </ul>
    <address class="address">88 Halden Avenue, Suite 310<br>Larkspur Heights, CA 90417</address>
  </section>
</main>
</body>
</html>
```